Mobile Fitness snd Therapy Business Card Design

I need a business card designed for my mobile fitness and therapy business.

Please view the images that I have uploaded. I like the simplicity of the design that I have attached. I adapted it with my information

Target Market(s)

Those seeking personal training, injury rehabilitation or massage therapy.

Industry/Entity Type

Business

Contact Information for Business Card

Dylan Marwick - MSc, CAT(C), RMT, CSCS, Pn2
e-mail: dylan@vantrelo.com
website: www.vantrelo.com
instagram: @dylan_marwick

Font styles to use
Sans Serif

Colors
3176b5
0355a3

Requirements
Must have
• "Contact us to receive a FREE assessment"
• Services offered:
• Personal Training
• Golf Fitness
• Injury Rehab
• Massage Therapy
• Yoga
Nice to have
• Consistent colours with brand
• - Dark Blue: #232837
• - Blue: #5096f0
• Consistent look/feel with the website: www.vantrelo.com

```html
<!DOCTYPE html>
<html lang="en">
<head>
<meta charset="utf-8">
<title>Vantrelo Business Card</title>
<link rel="stylesheet" href="https://fonts.googleapis.com/css2?family=Montserrat:wght@600;700&family=Open+Sans:wght@400;600&display=swap">
<style>
  :root {
    --navy: #232837;
    --blue: #3176b5;
    --blue-mid: #5096f0;
    --blue-deep: #0355a3;
    --ink: #1e2230;
    --paper: #ffffff;
    --backdrop: #e9eaec;
  }
  * { margin: 0; padding: 0; box-sizing: border-box; }
  html, body { width: 1200px; height: 1000px; overflow: hidden; }
  body { background: var(--backdrop); position: relative; font-family: "Open Sans", sans-serif; color: var(--ink); }

  .card { position: absolute; left: 266px; width: 666px; height: 397px; box-shadow: 0 4px 12px rgba(0,0,0,.18); }
  .card-front { top: 74px; background: var(--paper); }
  .card-back { top: 533px; background: var(--navy); }

  .side-tab { position: absolute; top: 129px; width: 13px; height: 139px; background: var(--navy); }
  .side-tab.left { left: 0; }
  .side-tab.right { right: 0; }

  .identity { position: absolute; left: 67px; top: 128px; }
  .person-name { font-family: "Montserrat", sans-serif; font-weight: 700; font-size: 20px; letter-spacing: .3px; color: var(--ink); }
  .credentials { font-size: 16.3px; color: var(--blue); margin-top: 1px; }
  .contact-list { list-style: none; margin-top: 17px; }
  .contact-list li { display: flex; align-items: center; gap: 8px; font-size: 17px; line-height: 25.5px; height: 25.5px; }
  .contact-list svg { width: 15px; height: 15px; flex: none; }

  .divider { position: absolute; left: 332px; top: 129px; width: 2px; height: 139px; background: var(--navy); }

  .services { position: absolute; left: 401px; top: 122px; list-style: none; }
  .services li { display: flex; align-items: center; gap: 10px; font-size: 18px; line-height: 30.3px; }
  .service-bullet { display: block; width: 7px; height: 7px; background: var(--blue); flex: none; }

  .call-to-action { position: absolute; left: 0; right: 0; top: 347px; text-align: center; font-size: 17.8px; }

  .brand { position: absolute; left: 0; right: 0; top: 159px; text-align: center; color: #fff; }
  .brand-name { font-family: "Montserrat", sans-serif; font-weight: 600; font-size: 58px; letter-spacing: 7px; line-height: 1; }
  .brand-tagline { font-family: "Montserrat", sans-serif; font-weight: 700; font-size: 18.5px; letter-spacing: 3.4px; margin-top: 8px; }
</style>
</head>
<body>
  <section class="card card-front">
    <span class="side-tab left"></span>
    <span class="side-tab right"></span>

    <div class="identity">
      <h1 class="person-name">DYLAN MARWICK</h1>
      <p class="credentials">MSc, CAT(C), RMT, CSCS, Pn2</p>
      <ul class="contact-list">
        <li><svg viewBox="0 0 15 15"><rect x="1" y="1" width="13" height="13" fill="var(--ink)"/></svg>@dylan_marwick</li>
        <li><svg viewBox="0 0 15 15"><rect x="1" y="3" width="13" height="9" fill="var(--ink)"/><path d="M1 3 L7.5 8.5 L14 3" fill="none" stroke="#fff" stroke-width="1.3"/></svg>dylan@vantrelo.com</li>
        <li><svg viewBox="0 0 15 15"><circle cx="7.5" cy="7.5" r="6" fill="none" stroke="var(--ink)" stroke-width="1.6"/><path d="M1.5 7.5h12M7.5 1.5c-3 3.5-3 8.5 0 12M7.5 1.5c3 3.5 3 8.5 0 12" fill="none" stroke="var(--ink)" stroke-width="1.2"/></svg>www.vantrelo.com</li>
      </ul>
    </div>

    <span class="divider"></span>

    <ul class="services">
      <li><span class="service-bullet"></span>Personal Training</li>
      <li><span class="service-bullet"></span>Golf Fitness</li>
      <li><span class="service-bullet"></span>Injury Rehab</li>
      <li><span class="service-bullet"></span>Massage Therapy</li>
      <li><span class="service-bullet"></span>Yoga</li>
    </ul>

    <p class="call-to-action">Contact us to receive a FREE assessment</p>
  </section>

  <section class="card card-back">
    <div class="brand">
      <p class="brand-name">VANTRELO</p>
      <p class="brand-tagline">NUTRITION - FITNESS - HEALTH</p>
    </div>
  </section>
</body>
</html>
```